Etiketten-Design für Gin
Zielgruppe
Herstellung von Spirituosen/ Molk UG (haftungsbeschränkt)
Zielgruppe: Vorwiegend Männer von 45 bis 70 Jahre
Aufgabenstellung
Flaschen Etikett Vorder- und Rückseite für Gin
Wortmarke: Dry Gin Molk sollte hervorgehoben sein.
Bedeutung hat für uns auch, dass er aus der Region Rhein-Main kommt.

```html
<!DOCTYPE html>
<html lang="de">
<head>
<meta charset="utf-8">
<title>Dry Gin Molk – Etiketten Vorder- und Rückseite</title>
<link rel="stylesheet" href="https://fonts.googleapis.com/css2?family=Alfa+Slab+One&family=Oswald:wght@600&family=Six+Caps&display=swap">
<style>
  :root {
    --paper: #ffffff;
    --label: #2f2f2f;
    --gold: #958462;
  }
  html, body {
    margin: 0;
    padding: 0;
    width: 1200px;
    height: 748px;
    overflow: hidden;
    background: var(--paper);
  }
  .canvas {
    position: relative;
    width: 1200px;
    height: 748px;
  }
  .label {
    position: absolute;
    top: 78px;
    width: 284px;
    height: 594px;
    display: block;
  }
  .label--front { left: 212px; }
  .label--back { left: 716px; }
  .label__ground { fill: var(--label); }
  .rule { stroke: var(--gold); fill: none; }
  .ornament { fill: var(--gold); }
  .brand-arc, .wordmark, .origin, .volume, .subline {
    font-family: "Six Caps", "Oswald", sans-serif;
    fill: var(--gold);
  }
  .story {
    font-family: "Alfa Slab One", "Rockwell", serif;
    fill: var(--gold);
    text-anchor: middle;
  }
  .legal {
    font-family: "Oswald", "Arial Narrow", sans-serif;
    font-weight: 600;
    fill: var(--gold);
  }
</style>
</head>
<body>
<main class="canvas">

  <!-- Vorderseite -->
  <svg class="label label--front" viewBox="0 0 284 594" aria-label="Etikett Vorderseite">
    <defs>
      <path id="front-brand-path" d="M30 150 Q146 68 262 150"/>
      <path id="front-origin-path" d="M60 413 Q143 444 226 413"/>
    </defs>
    <rect class="label__ground" width="284" height="594"/>

    <path class="rule" stroke-width="2" d="M17 118 Q146 3 274 118"/>
    <text class="brand-arc" font-size="40">
      <textPath href="#front-brand-path" startOffset="50%" text-anchor="middle">DESTILLERIE MOLK</textPath>
    </text>
    <path class="rule" stroke-width="2" d="M64 161 Q146 86 227 161"/>

    <text class="wordmark" x="15" y="309" font-size="104" textLength="259" lengthAdjust="spacingAndGlyphs">DRY GIN MOLK</text>
    <line class="rule" stroke-width="2" x1="10" y1="314" x2="275" y2="314"/>

    <polygon class="ornament" points="143,353 151,368 143,383 135,368"/>

    <text class="origin" font-size="30">
      <textPath href="#front-origin-path" startOffset="50%" text-anchor="middle">DISTILLED IN GERMANY</textPath>
    </text>

    <g class="rule" stroke-width="2">
      <line x1="11" y1="518" x2="273" y2="518"/>
      <line x1="11" y1="557" x2="273" y2="557"/>
      <line x1="11" y1="527" x2="51" y2="527"/>
      <line x1="11" y1="537" x2="51" y2="537"/>
      <line x1="11" y1="547" x2="51" y2="547"/>
      <line x1="233" y1="527" x2="273" y2="527"/>
      <line x1="233" y1="537" x2="273" y2="537"/>
      <line x1="233" y1="547" x2="273" y2="547"/>
    </g>
    <text class="volume" x="68" y="548" font-size="28" textLength="31" lengthAdjust="spacingAndGlyphs">35 CL</text>
    <polygon class="ornament" points="141,528 147,538 141,549 135,538"/>
    <text class="volume" x="175" y="548" font-size="28" textLength="52" lengthAdjust="spacingAndGlyphs">45 % VOL.</text>
  </svg>

  <!-- Rückseite -->
  <svg class="label label--back" viewBox="0 0 284 594" aria-label="Etikett Rückseite">
    <defs>
      <path id="back-brand-path" d="M36 105 Q144 35 252 105"/>
    </defs>
    <rect class="label__ground" width="284" height="594"/>

    <path class="rule" stroke-width="2" d="M21 74 Q144 -37 266 74"/>
    <text class="brand-arc" font-size="38">
      <textPath href="#back-brand-path" startOffset="50%" text-anchor="middle">DESTILLERIE MOLK</textPath>
    </text>
    <path class="rule" stroke-width="2" d="M66 115 Q144 43 221 115"/>

    <polygon class="ornament" points="49,143 54,152 49,161 44,152"/>
    <text class="wordmark" x="88" y="172" font-size="48" textLength="119" lengthAdjust="spacingAndGlyphs">DRY GIN MOLK</text>
    <line class="rule" stroke-width="1.2" x1="86" y1="175" x2="208" y2="175"/>
    <polygon class="ornament" points="248,143 253,152 248,161 243,152"/>

    <text class="subline" x="108" y="206" font-size="23" textLength="72" lengthAdjust="spacingAndGlyphs">WESTERN DRY GIN</text>

    <g class="story" font-size="19">
      <text x="143" y="247" textLength="208" lengthAdjust="spacingAndGlyphs">EIN ERLESENER GIN AUS</text>
      <text x="143" y="274" textLength="145" lengthAdjust="spacingAndGlyphs">DEM HERZEN DES</text>
      <text x="143" y="300" textLength="222" lengthAdjust="spacingAndGlyphs">RHEIN-MAIN GEBIETES, IM</text>
      <text x="143" y="327" textLength="200" lengthAdjust="spacingAndGlyphs">KUPFERKESSEL 2-FACH</text>
      <text x="143" y="353" textLength="118" lengthAdjust="spacingAndGlyphs">DESTILLIERT.</text>
      <text x="143" y="380" textLength="209" lengthAdjust="spacingAndGlyphs">ER SCHMECKT DEUTLICH</text>
      <text x="143" y="406" textLength="242" lengthAdjust="spacingAndGlyphs">NACH ZITRUSNOTEN, LEICHT</text>
      <text x="143" y="433" textLength="207" lengthAdjust="spacingAndGlyphs">PFEFFRIG UND ENTHÄLT</text>
      <text x="143" y="460" textLength="242" lengthAdjust="spacingAndGlyphs">SUBTIL HERBE BOTANICALS.</text>
    </g>

    <text class="legal" x="25" y="489" font-size="14" textLength="240" lengthAdjust="spacingAndGlyphs">Destilliert und abgefüllt in Deutschland.</text>
    <text class="legal" x="25" y="502" font-size="8.5" textLength="240" lengthAdjust="spacingAndGlyphs">Erzeugerbetrieb: Molk UG (haftungsbeschränkt), D-60999 Feldau</text>

    <g class="rule" stroke-width="2">
      <line x1="11" y1="517" x2="273" y2="517"/>
      <line x1="11" y1="556" x2="273" y2="556"/>
      <line x1="11" y1="527" x2="40" y2="527"/>
      <line x1="11" y1="537" x2="40" y2="537"/>
      <line x1="11" y1="547" x2="40" y2="547"/>
      <line x1="245" y1="527" x2="273" y2="527"/>
      <line x1="245" y1="537" x2="273" y2="537"/>
      <line x1="245" y1="547" x2="273" y2="547"/>
    </g>
    <text class="legal" x="51" y="542" font-size="13" textLength="27" lengthAdjust="spacingAndGlyphs">35 cl</text>
    <rect class="ornament" x="94" y="527" width="97" height="21"/>
    <text class="legal" x="199" y="542" font-size="12" textLength="41" lengthAdjust="spacingAndGlyphs">45 % Vol.</text>
  </svg>

</main>
</body>
</html>
```